FREIGHT FORWARDING FLYER

We need a flyer designed for our company (Brightwell Freight Global) showing the list of services we offer to hand out to customers. Below is a list of services:<br/><br/>-Ocean/Air Import and Export<br/>-Exhibition Cargo<br/>-Carnet Application<br/>-Project Cargo (OOG/Flatrack/Reefer/DG)<br/>-Customs Clearance<br/>-Door to Door Services<br/>-Cargo Insurance<br/>-Warehousing<br/>-Trucking (LTL/FCL)

Target Market(s)

Customers who have a specific need for freight forwarding, especially customers at exhibitions.

Industry/Entity Type

Freight Forwarding

Colors

Designer to choose colors to be used in the design.

Requirements
Must have
• The services we offer need to pop to the customer and essentially get that interested in the services we offer.

```html
<!DOCTYPE html>
<html lang="en">
<head>
<meta charset="utf-8">
<title>Brightwell Freight Global – Services Flyer</title>
<link href="https://fonts.googleapis.com/css2?family=Bebas+Neue&family=Lato:wght@700&family=Montserrat:wght@700&family=Roboto+Condensed:wght@400&display=swap" rel="stylesheet">
<style>
  :root {
    --red: #e51e25;
    --charcoal: #2a2a2c;
    --ink: #222222;
    --grey-text: #5f6062;
    --paper-top: #ececec;
    --paper: #ffffff;
    --white: #ffffff;
    --stripe: #4a4a4c;
  }
  * { margin: 0; padding: 0; box-sizing: border-box; }
  html, body { width: 902px; height: 1200px; overflow: hidden; background: var(--paper); }
  .flyer {
    position: relative; width: 902px; height: 1200px; overflow: hidden;
    background: linear-gradient(180deg, var(--paper-top) 0%, var(--paper) 30%);
    font-family: "Lato", Arial, sans-serif;
  }
  .shapes { position: absolute; inset: 0; }

  .brand { position: absolute; top: 58px; left: 0; width: 100%; display: flex; justify-content: center; align-items: center; gap: 22px; }
  .brand-mark { width: 96px; height: 96px; background: var(--red); }
  .brand-name {
    font-family: "Roboto Condensed", Arial, sans-serif; font-weight: 400;
    font-size: 34px; line-height: 36px; letter-spacing: 1px; color: var(--grey-text); text-transform: uppercase;
  }

  .transport-visual {
    position: absolute; left: 0; top: 300px; width: 470px; height: 300px;
    background: radial-gradient(ellipse at 45% 55%, #6f8fc7 0%, #9fb1cf 35%, #e3e8ef 65%, rgba(255,255,255,0) 80%);
  }

  .headline { position: absolute; left: 500px; top: 352px; width: 350px; text-align: center; }
  .headline-lead { font-family: "Bebas Neue", Impact, sans-serif; font-size: 50px; line-height: 52px; color: var(--ink); }
  .headline-main { font-family: "Montserrat", Arial, sans-serif; font-weight: 700; font-size: 47px; line-height: 60px; color: var(--white); }

  .services { position: absolute; left: 417px; top: 640px; list-style: none; }
  .services li { display: flex; align-items: center; height: 47.4px; color: var(--white); font-size: 20px; font-weight: 700; }
  .services svg { width: 19px; height: 19px; margin-right: 13px; flex: none; }

  .contact { position: absolute; left: 40px; width: 266px; text-align: center; color: var(--ink); font-weight: 700; }
  .contact-icon { display: block; width: 62px; height: 62px; margin: 0 auto; }
  .contact-phone { top: 692px; font-size: 25px; }
  .contact-phone .contact-icon { margin-bottom: 22px; }
  .contact-email { top: 862px; font-size: 18px; }
  .contact-email .contact-icon { margin-bottom: 26px; }

  .footer-line {
    position: absolute; left: 0; width: 100%; top: 1131px; text-align: center;
    font-size: 21px; font-weight: 700; color: var(--ink);
  }
  .footer-line .web { color: var(--white); margin-left: 6px; }
  .footer-line svg { width: 18px; height: 18px; vertical-align: -2px; margin-left: 6px; }
</style>
</head>
<body>
<main class="flyer">
  <svg class="shapes" viewBox="0 0 902 1200" aria-hidden="true">
    <path d="M0,600 Q220,632 408,610 L404,622 Q200,646 0,626 Z" fill="var(--red)"/>
    <path d="M517,292 Q720,318 902,350 L902,512 Q650,590 408,606 Q425,420 517,292 Z" fill="var(--red)"/>
    <path d="M408,606 Q650,590 902,508 L902,1048 Q640,1070 368,1094 Q350,850 408,606 Z" fill="var(--charcoal)"/>
    <path d="M0,290 Q370,190 902,345 L902,358 Q380,222 0,318 Z" fill="var(--red)"/>
    <path d="M0,1020 Q120,1070 380,1080 Q640,1080 902,1040 L902,1052 Q640,1092 380,1094 Q120,1092 0,1044 Z" fill="var(--stripe)"/>
    <path d="M0,1056 Q160,1110 420,1108 Q680,1104 902,1058 L902,1200 L0,1200 Z" fill="var(--red)"/>
  </svg>

  <header class="brand">
    <span class="brand-mark"></span>
    <div class="brand-name">Brightwell<br>Freight<br>Global</div>
  </header>

  <div class="transport-visual" role="img" aria-label="Airplane, high-speed train, blue freight truck and cargo ship grouped together"></div>

  <h1 class="headline">
    <span class="headline-lead">Below is a list of</span><br>
    <span class="headline-main">SERVICES<br>WE OFFER</span>
  </h1>

  <ul class="services">
    <li><svg viewBox="0 0 20 20"><circle cx="10" cy="10" r="10" fill="var(--red)"/><path d="M8 6l4 4-4 4" stroke="var(--charcoal)" stroke-width="2.2" fill="none"/></svg>Ocean/Air Import and Export</li>
    <li><svg viewBox="0 0 20 20"><circle cx="10" cy="10" r="10" fill="var(--red)"/><path d="M8 6l4 4-4 4" stroke="var(--charcoal)" stroke-width="2.2" fill="none"/></svg>Exhibition Cargo</li>
    <li><svg viewBox="0 0 20 20"><circle cx="10" cy="10" r="10" fill="var(--red)"/><path d="M8 6l4 4-4 4" stroke="var(--charcoal)" stroke-width="2.2" fill="none"/></svg>Carnet Application</li>
    <li><svg viewBox="0 0 20 20"><circle cx="10" cy="10" r="10" fill="var(--red)"/><path d="M8 6l4 4-4 4" stroke="var(--charcoal)" stroke-width="2.2" fill="none"/></svg>Project Cargo (OOG/Flatrack/Reefer/DG)</li>
    <li><svg viewBox="0 0 20 20"><circle cx="10" cy="10" r="10" fill="var(--red)"/><path d="M8 6l4 4-4 4" stroke="var(--charcoal)" stroke-width="2.2" fill="none"/></svg>Customs Clearance</li>
    <li><svg viewBox="0 0 20 20"><circle cx="10" cy="10" r="10" fill="var(--red)"/><path d="M8 6l4 4-4 4" stroke="var(--charcoal)" stroke-width="2.2" fill="none"/></svg>Door to Door Services</li>
    <li><svg viewBox="0 0 20 20"><circle cx="10" cy="10" r="10" fill="var(--red)"/><path d="M8 6l4 4-4 4" stroke="var(--charcoal)" stroke-width="2.2" fill="none"/></svg>Cargo Insurance</li>
    <li><svg viewBox="0 0 20 20"><circle cx="10" cy="10" r="10" fill="var(--red)"/><path d="M8 6l4 4-4 4" stroke="var(--charcoal)" stroke-width="2.2" fill="none"/></svg>Warehousing</li>
    <li><svg viewBox="0 0 20 20"><circle cx="10" cy="10" r="10" fill="var(--red)"/><path d="M8 6l4 4-4 4" stroke="var(--charcoal)" stroke-width="2.2" fill="none"/></svg>Trucking (LTL/FCL)</li>
  </ul>

  <div class="contact contact-phone">
    <svg class="contact-icon" viewBox="0 0 62 62" aria-hidden="true">
      <circle cx="31" cy="31" r="30" fill="var(--red)"/>
      <circle cx="31" cy="31" r="20" fill="none" stroke="var(--white)" stroke-width="2"/>
      <path d="M24 21c2-1 3 0 4 3s0 3-1 4c1 3 3 5 6 6 1-1 2-2 4-1s4 2 3 4c-1 3-4 4-7 3-6-2-10-7-11-12 0-3 1-6 2-7z" fill="var(--white)"/>
    </svg>
    1234567890
  </div>

  <div class="contact contact-email">
    <svg class="contact-icon" viewBox="0 0 62 62" aria-hidden="true">
      <circle cx="31" cy="31" r="30" fill="var(--red)"/>
      <rect x="16" y="21" width="30" height="20" fill="var(--white)"/>
      <path d="M16 21l15 12 15-12M16 41l11-10M46 41l-11-10" stroke="var(--red)" stroke-width="1.6" fill="none"/>
    </svg>
    hello@brightwellfreight.com
  </div>

  <p class="footer-line">For more information please visit :
    <svg viewBox="0 0 20 20" aria-hidden="true"><circle cx="10" cy="10" r="8.5" fill="none" stroke="var(--white)" stroke-width="1.6"/><ellipse cx="10" cy="10" rx="3.5" ry="8.5" fill="none" stroke="var(--white)" stroke-width="1.4"/><path d="M1.5 10h17M3 5.5h14M3 14.5h14" stroke="var(--white)" stroke-width="1.2"/></svg>
    <span class="web">www.brightwellfreight.com</span>
  </p>
</main>
</body>
</html>
```